Standout Business Card for Recruiting New Hires

JOIN A WINNING TEAM! We are a nationally recognized Top Contractor for Paving and Parking Lot Maintenance. Our people are our most valuable asset, helping us to achieve Our Vision of building the best commercial pavement services company to benefit the best owners, the best employees and the best customers.

We want to create a Business Card to help us capture potential new hires, whenever and wherever they are discovered. This is not a traditional business card with someone's name it, only our Company Name and the information provided below.

Target Market(s)

Exceptional, standout, customer service oriented employees currently working elsewhere...at our competitors, at the car wash, in the deli, at the restaurant, in an airport, driving an Tripzel...wherever we find them.

Industry/Entity Type

Construction Company

Contact Information for Business Card

A double sided business card, with the standout feature being "Join A Winning Team" and the benefits listed somewhere on the card.

Requirements
Must have
• -Call to Action (Join a Winning Team)
• -Our Logo
• -Our Physical Address (17B Harrow Court, Clinton, CT 06287)
• -Our Website (www.BrightfieldSurfacing.com)
• -Our Phone Number (860) 555-0147.
• -Our Bullet Points (can be altered):
• - Competitive Pay
• - Full Time, Consistent Work Schedule
• - Paid Overtime / Drive Time
• - Work with Great People in a Great Environment
• - Training Program
• Something like that.
Nice to have
• Maybe it could say, "Come and Join Connecticut's Top Rated Paving Contractor" or Come grow with us. Something like that.
Should not have
• Anyone's name on it. This is a generic card for anyone at the company to give to a potential employee! (I have attached a business card sample, just to illustrate our look and feel).

```html
<!DOCTYPE html>
<html lang="en">
<head>
<meta charset="utf-8">
<title>Brightfield Surfacing – Recruiting Card</title>
<link href="https://fonts.googleapis.com/css2?family=Source+Sans+3:wght@400;600;700&display=swap" rel="stylesheet">
<style>
  :root {
    --backdrop: #4a3324;
    --card-dark: #000000;
    --card-light: #ffffff;
    --brand-red: #b8211f;
    --ink: #111111;
    --ink-soft: #555555;
    --on-dark: #ffffff;
  }
  * { box-sizing: border-box; margin: 0; padding: 0; }
  html, body {
    width: 1200px; height: 1000px; overflow: hidden;
    background: var(--backdrop);
    font-family: "Source Sans 3", "Myriad Pro", Arial, sans-serif;
  }
  .card {
    position: absolute; left: 284px; width: 632px; height: 360px;
    box-shadow: 0 6px 14px rgba(0,0,0,.45);
  }
  .card--front { top: 124px; background: var(--card-dark); }
  .card--back  { top: 516px; background: var(--card-light); }

  .brand { display: flex; align-items: center; gap: 10px; }
  .brand__dot { border-radius: 50%; background: var(--brand-red); flex: none; }
  .brand__name { font-weight: 700; line-height: 1; white-space: nowrap; }

  .card--front .brand {
    position: absolute; top: 138px; left: 0; right: 0; justify-content: center;
  }
  .card--front .brand__dot { width: 44px; height: 44px; }
  .card--front .brand__name { color: var(--on-dark); font-size: 44px; }
  .front__web {
    position: absolute; left: 0; right: 0; top: 312px; text-align: center;
    color: var(--on-dark); font-weight: 600; font-size: 18px; letter-spacing: .2px;
  }

  .card--back .brand { position: absolute; left: 20px; top: 26px; }
  .card--back .brand__dot { width: 32px; height: 32px; }
  .card--back .brand__name { color: var(--ink); font-size: 32px; }

  .benefits {
    position: absolute; left: 28px; top: 102px; width: 600px;
    color: var(--ink-soft); font-size: 17px; line-height: 21px;
    letter-spacing: .15px; white-space: nowrap;
  }
  .benefits .sep { color: var(--brand-red); margin: 0 8px; }

  .call-to-action {
    position: absolute; right: 347px; top: 274px; text-align: right;
    color: var(--ink); font-size: 16px; line-height: 22px; white-space: nowrap;
  }
  .call-to-action__headline { font-weight: 700; font-size: 17px; }
  .contact-divider {
    position: absolute; left: 315px; top: 266px; bottom: 0;
    width: 1.5px; background: var(--ink);
  }
  .contact-details {
    position: absolute; left: 343px; top: 274px;
    color: var(--ink); font-size: 16px; line-height: 21px; white-space: nowrap;
  }
</style>
</head>
<body>
  <section class="card card--front" aria-label="Card front">
    <div class="brand">
      <span class="brand__dot"></span>
      <span class="brand__name">Brightfield Surfacing</span>
    </div>
    <p class="front__web">www.brightfieldsurfacing.com</p>
  </section>

  <section class="card card--back" aria-label="Card back">
    <div class="brand">
      <span class="brand__dot"></span>
      <span class="brand__name">Brightfield Surfacing</span>
    </div>
    <p class="benefits">
      Competitive Pay<span class="sep">|</span>Full Time, Consistent Work Schedule<span class="sep">|</span>Training Program<br>
      Paid Overtime / Drive Time<span class="sep">|</span>Work with Great People in a Great Environment
    </p>
    <div class="call-to-action">
      <p class="call-to-action__headline">Join A Winning Team!</p>
      <p>Come grow with us</p>
    </div>
    <div class="contact-divider"></div>
    <div class="contact-details">
      <p>17B Harrow Court, Clinton, CT 06287</p>
      <p>T: 860.555.0147</p>
      <p>E: careers@brightfieldsurfacing.com</p>
    </div>
  </section>
</body>
</html>
```